Need a pull up Banner to promote a fiction book

We need a design for a pull up banner (850mm x 2000mm) to promote a fiction book (Novel) with the author.

The book is a mystical/mythical/fantacy novel.

will attache images of the novel and the author

need the source fils in ai format

```html
<!DOCTYPE html>
<html lang="en">
<head>
<meta charset="utf-8">
<title>The Shard of Veils – Pull-up Banner</title>
<link rel="stylesheet" href="https://fonts.googleapis.com/css2?family=Cinzel:wght@400;500&family=Cormorant+Garamond:ital,wght@0,500;1,500&display=swap">
<style>
  :root {
    --navy-deep: #080a18;
    --navy: #111733;
    --sky: #43abe2;
    --white: #ffffff;
    --page: #f1f1f1;
    --ink: #0c1230;
  }
  html, body {
    margin: 0;
    padding: 0;
    width: 1200px;
    height: 4000px;
    overflow: hidden;
    background: var(--page);
  }
  .banner {
    position: absolute;
    left: 0;
    top: 589px;
    width: 1200px;
    height: 2822px;
    box-shadow: 0 10px 40px rgba(0,0,0,0.18);
  }
  .banner svg { display: block; }
  .title {
    font-family: "Cinzel", "Times New Roman", serif;
    font-weight: 500;
    fill: var(--white);
  }
  .subtitle {
    font-family: "Cormorant Garamond", Georgia, serif;
    font-weight: 500;
    fill: var(--sky);
  }
  .subtitle .of { font-style: italic; }
  .author {
    font-family: "Cinzel", "Times New Roman", serif;
    font-weight: 500;
    fill: var(--ink);
  }
</style>
</head>
<body>
<main class="banner">
  <svg width="1200" height="2822" viewBox="0 0 1200 2822" xmlns="http://www.w3.org/2000/svg">
    <defs>
      <linearGradient id="night-sky" x1="0" y1="0" x2="0" y2="1">
        <stop offset="0" stop-color="#070916"/>
        <stop offset="1" stop-color="#141b3a"/>
      </linearGradient>
      <linearGradient id="frost" x1="0" y1="0" x2="0" y2="1">
        <stop offset="0" stop-color="#ffffff"/>
        <stop offset="0.45" stop-color="#f4f5f7"/>
        <stop offset="0.75" stop-color="#dcdee3"/>
        <stop offset="1" stop-color="#eceef1"/>
      </linearGradient>
      <linearGradient id="portrait-tones" x1="0" y1="0" x2="0" y2="1">
        <stop offset="0" stop-color="#2a1c17"/>
        <stop offset="0.25" stop-color="#a87a5e"/>
        <stop offset="0.42" stop-color="#2a1d19"/>
        <stop offset="1" stop-color="#0d0c0e"/>
      </linearGradient>
      <linearGradient id="cover-tones" x1="0" y1="0" x2="0" y2="1">
        <stop offset="0" stop-color="#6f7c90"/>
        <stop offset="0.5" stop-color="#c4c8cf"/>
        <stop offset="1" stop-color="#1f2a4a"/>
      </linearGradient>
      <linearGradient id="device-tones" x1="0" y1="0" x2="0" y2="1">
        <stop offset="0" stop-color="#1d1e22"/>
        <stop offset="1" stop-color="#2c2e33"/>
      </linearGradient>
    </defs>

    <!-- background layers -->
    <rect class="frost-field" x="0" y="0" width="1200" height="2822" fill="url(#frost)"/>
    <path class="sky-swoosh-left" d="M0 1200 L0 1395 Q200 1420 380 1430 Q150 1390 0 1229 Z" fill="var(--sky)"/>
    <path class="sky-swoosh-right" d="M1200 1230 L1200 1312 Q1100 1385 960 1420 Q1110 1350 1200 1253 Z" fill="var(--sky)"/>
    <path class="night-field" d="M0 0 H1200 V1253 Q600 1720 0 1229 Z" fill="url(#night-sky)"/>

    <path class="navy-swoosh-left" d="M0 2181 Q200 2040 470 2000 Q180 2110 0 2318 Z" fill="var(--navy)"/>
    <path class="navy-swoosh-right" d="M1200 2055 L1200 2135 Q1020 2095 860 2108 Q1060 2070 1200 2055 Z" fill="var(--navy)"/>
    <path class="sky-base" d="M0 2308 Q500 2020 1200 2133 V2822 H0 Z" fill="var(--sky)"/>

    <!-- title block -->
    <text class="title" x="600" y="223" text-anchor="middle" font-size="163">THE</text>
    <text class="title" x="600" y="453" text-anchor="middle" font-size="260" textLength="945" lengthAdjust="spacingAndGlyphs">SHARD</text>
    <text class="title" x="600" y="616" text-anchor="middle" font-size="156">OF</text>
    <text class="title" x="600" y="846" text-anchor="middle" font-size="256">VEILS</text>
    <text class="subtitle" x="600" y="999" text-anchor="middle" font-size="112" textLength="904" lengthAdjust="spacingAndGlyphs">New Age <tspan class="of">of</tspan> Varneth</text>

    <!-- author portrait -->
    <path class="author-portrait" role="img" aria-label="Portrait photograph of the author, smiling, with long dark hair and a black top"
          d="M520 1059 Q400 1070 380 1250 Q370 1420 420 1520 Q250 1560 200 1680 Q150 1800 136 2060 H1020 Q1010 1800 960 1680 Q900 1560 760 1520 Q790 1400 780 1250 Q760 1070 640 1059 Z"
          fill="url(#portrait-tones)"/>

    <!-- book formats mockup -->
    <g class="book-mockup" role="img" aria-label="Mockup of the novel as paperback, tablet and phone e-book showing the cover">
      <rect class="tablet" x="148" y="1975" width="405" height="595" rx="22" fill="url(#device-tones)"/>
      <rect class="tablet-screen" x="182" y="2030" width="337" height="485" fill="url(#cover-tones)"/>
      <rect class="paperback" x="532" y="1859" width="472" height="732" rx="6" fill="url(#cover-tones)"/>
      <rect class="paperback-edge" x="984" y="1866" width="20" height="725" fill="#d9d2c6"/>
      <rect class="phone" x="400" y="2155" width="225" height="436" rx="26" fill="url(#device-tones)"/>
      <rect class="phone-screen" x="416" y="2205" width="193" height="336" fill="url(#cover-tones)"/>
    </g>

    <!-- author name -->
    <text class="author" x="600" y="2700" text-anchor="middle" font-size="84" textLength="970" lengthAdjust="spacingAndGlyphs">MARA ELWIN SATHE</text>
  </svg>
</main>
</body>
</html>
```